Korvel Professional Services Website

Small website for company presence and information. Company is an IT/Telecom services company. We provide presales and installation services. Included are various company logos including color levels. Site doesn't have to use these exact colors in the logos, but should be complimentary if using different colors. It should have a professional business appearance.
Updates

My apologies for not being more responsive on the designs that have been submitted. I will be narrowing down the submissions and providing additional feedback next week. Thank you for your patience.

Project Deadline Extended
Reason: Sorry again for delays on picking designs. Work has me very busy and I've just not had the time to devote to this project. I am extending the design deadline for a few more days to give me time to make my final decisions. Thank you all for your patience. Stay tuned....

Target Market(s)

Telecom sales companies that sell Quenti telecom products.

Industry/Entity Type

Professional Service

Coding

Coded - Design and coding required

Number of Pages Required

5+ page

Font styles to use
Sans Serif

Colors
3276b5
0355a3
85abd2
85cae6
33a6d7
0692cd
ffffff

Requirements
Must have
• Professional design reflective of IT/Telecom business. A good reference website would be: http://www.lorbextech.example/. Looking for something similar in function and presence.
Nice to have
• Rolling photos highlighting our services. Traditional navigation across the top of all pages.
Should not have
• No motion video, flashy presentation or overly confused interface.

```html
<!DOCTYPE html>
<html lang="en">
<head>
<meta charset="utf-8">
<title>Korvel Professional Services</title>
<link href="https://fonts.googleapis.com/css2?family=Exo+2:wght@500;600;700;800&family=Open+Sans:wght@400;600;700&display=swap" rel="stylesheet">
<style>
:root{
  --navy:#1d2b64;
  --navy-deep:#0f1a42;
  --blue:#2676b9;
  --blue-light:#3a8fd0;
  --grey-bg:#f4f4f4;
  --grey-line:#d8d8d8;
  --text:#555a63;
  --white:#ffffff;
}
*{margin:0;padding:0;box-sizing:border-box}
html,body{width:1200px;height:2980px;overflow:hidden;background:var(--white)}
body{font-family:"Open Sans",Arial,sans-serif;color:var(--text);position:relative}
.abs{position:absolute}

.top-bar{left:0;top:0;width:1200px;height:44px;background:var(--navy)}
.top-bar .contact-item{top:13px;color:var(--white);font-size:13px;display:flex;align-items:center;gap:8px}
.site-header{left:0;top:44px;width:1200px;height:102px;background:var(--white)}
.brand{left:80px;top:34px;display:flex;align-items:center;gap:12px;font-family:"Exo 2",sans-serif;font-weight:800;font-size:24px;color:var(--navy);letter-spacing:.5px}
.brand .mark{width:26px;height:26px;background:var(--blue)}
.main-nav a{position:absolute;top:57px;font-family:"Exo 2",sans-serif;font-weight:700;font-size:15px;color:var(--navy);text-decoration:none;letter-spacing:.3px}
.main-nav a.active{color:var(--blue)}
.nav-marker{left:561px;top:73px;width:18px;height:18px;background:var(--blue)}

.hero{left:0;top:146px;width:1200px;height:530px;background:linear-gradient(135deg,#e9edf2 0%,#c9d1dc 40%,#dfe4ea 70%,#b9c2cd 100%);clip-path:polygon(0 0,100% 0,100% 78%,1110px 100%,90px 100%,0 78%)}
.hero-hex{left:384px;top:178px;width:434px;height:416px}
.hero-title{left:384px;top:300px;width:434px;text-align:center;font-family:"Exo 2",sans-serif;font-weight:600;font-size:32px;line-height:43px;color:var(--white);letter-spacing:.5px}
.hero-dots{left:574px;top:500px;display:flex;gap:4px}
.hero-dots span{width:15px;height:15px;background:var(--white);clip-path:polygon(25% 0,75% 0,100% 50%,75% 100%,25% 100%,0 50%)}
.hero-dots span+span{opacity:.7}

.section-title{left:0;width:1200px;text-align:center;font-family:"Exo 2",sans-serif;font-weight:700;font-size:35px;color:var(--navy);letter-spacing:.3px}
.section-title em{font-style:normal;color:var(--blue)}
.divider{width:268px;height:14px;left:466px}
.divider::before{content:"";position:absolute;left:0;right:0;top:7px;height:1px;background:var(--grey-line)}
.divider::after{content:"";position:absolute;left:127px;top:0;width:14px;height:14px;border-radius:50%;background:var(--navy);box-shadow:0 0 0 5px var(--white)}
.divider.on-grey::after{box-shadow:0 0 0 5px var(--grey-bg)}
.lead{left:100px;width:1000px;text-align:center;font-weight:700;font-size:13.5px;line-height:22px;color:var(--navy)}

.about-text{left:80px;top:878px;width:664px;font-size:12.4px;line-height:24.6px;color:var(--text)}
.btn-more{left:80px;top:1085px;height:32px;display:flex;align-items:center}
.btn-more .icon{width:30px;height:32px;background:var(--navy);clip-path:polygon(50% 0,100% 25%,100% 75%,50% 100%,0 75%,0 25%)}
.btn-more .label{height:28px;line-height:28px;padding:0 14px 0 10px;margin-left:-4px;background:var(--navy);color:var(--white);font-family:"Exo 2",sans-serif;font-weight:700;font-size:13px;letter-spacing:.3px}
.video{left:767px;top:876px;width:352px;height:239px;background:var(--navy-deep)}
.video .frame{left:0;top:0;width:352px;height:212px;background:linear-gradient(135deg,#1f2a3a 0%,#4f6279 45%,#8da0b6 70%,#2b3646 100%)}
.video .play{left:151px;top:84px;width:50px;height:36px;border-radius:8px;background:rgba(15,26,66,.8)}
.video .play::after{content:"";position:absolute;left:19px;top:10px;border-left:15px solid var(--white);border-top:8px solid transparent;border-bottom:8px solid transparent}
.video .controls{left:0;top:212px;width:352px;height:27px;background:#111}
.controls .time{top:7px;color:var(--white);font-size:10px}
.controls .track{left:84px;top:12px;width:164px;height:4px;background:#555}
.controls .track span{display:block;width:100px;height:4px;background:#e52d27}

.services{left:0;top:1113px;width:1200px;height:568px;background:var(--grey-bg);clip-path:polygon(0 0,90px 50px,1110px 50px,1200px 0,100% 100%,0 100%)}
.service{width:230px;text-align:center}
.service svg{display:block;margin:0 auto}
.service h3{margin-top:16px;font-family:"Exo 2",sans-serif;font-weight:600;font-size:17px;line-height:23px;color:var(--navy)}
.offer-card{top:1735px;width:512px;height:306px;background:#e4e5e6;padding:14px}
.offer-card .photo{width:100%;height:100%;display:flex;align-items:center;justify-content:center;font-family:"Exo 2",sans-serif;font-weight:700;font-size:34px;color:var(--white);letter-spacing:.5px;text-shadow:0 2px 6px rgba(0,0,0,.35)}
.presales .photo{background:linear-gradient(135deg,#1c3e55 0%,#2f7f97 50%,#15324a 100%)}
.install .photo{background:linear-gradient(135deg,#27303d 0%,#4c5f74 50%,#1b2230 100%)}

.testimonials{left:0;top:2102px;width:1200px;height:520px;background:var(--grey-bg)}
.client{width:180px;text-align:center;top:2250px}
.client svg{display:block;margin:0 auto}
.client .name{margin-top:10px;font-size:14px;color:#999}
.client.active .name{color:var(--blue);font-weight:700}
.arrow{top:2302px;width:16px;height:30px}
.quote-box{left:80px;top:2444px;width:1039px;height:136px;background:var(--white);border:1px solid var(--grey-line)}
.quote-box::before{content:"";position:absolute;left:192px;top:-12px;width:22px;height:22px;background:var(--white);border-left:1px solid var(--grey-line);border-top:1px solid var(--grey-line);transform:rotate(45deg)}
.quote-box p{position:absolute;left:36px;top:26px;width:967px;text-align:center;font-size:14px;line-height:28px;color:var(--text);text-indent:40px}
.quote-mark{font-family:Georgia,serif;font-size:54px;color:#cfd3d8;line-height:1}

.site-footer{left:0;top:2573px;width:1200px;height:358px;background:var(--navy);clip-path:polygon(0 0,90px 60px,1110px 60px,1200px 0,100% 100%,0 100%)}
.footer-col h4{font-family:"Exo 2",sans-serif;font-weight:700;font-size:17px;color:var(--white);letter-spacing:.3px;padding-bottom:10px;border-bottom:1px solid #34427a}
.footer-col h4 em{font-style:normal;color:var(--blue-light)}
.quick-links li{list-style:none;position:absolute;left:0;font-size:13px;color:var(--white)}
.quick-links li.current{color:var(--blue-light)}
.footer-text{font-size:13px;color:var(--white)}
.field{left:580px;width:267px;background:#18245a;color:#8c96bd;font-size:12px;padding:10px 14px}
.btn-submit{left:580px;top:2863px;width:108px;height:34px;background:var(--blue);color:var(--white);font-family:"Exo 2",sans-serif;font-weight:700;font-size:15px;text-align:center;line-height:34px}
.footer-brand{left:905px;top:2770px;width:220px;display:flex;align-items:center;gap:10px;font-family:"Exo 2",sans-serif;font-weight:700;font-size:19px;line-height:24px;color:var(--white)}
.footer-brand .mark{flex:0 0 22px;height:22px;background:var(--blue-light)}
.bottom-bar{left:0;top:2931px;width:1200px;height:49px;background:var(--navy-deep)}
.bottom-bar .copy{left:80px;top:17px;font-size:12px;color:#c8cde0}
.social{top:12px;width:26px;height:26px;border-radius:50%;background:var(--blue);border:2px solid var(--white)}
</style>
</head>
<body>

<div class="abs top-bar">
  <div class="abs contact-item" style="left:814px">
    <svg width="13" height="13" viewBox="0 0 24 24"><path fill="#fff" d="M6.6 10.8a15.1 15.1 0 0 0 6.6 6.6l2.2-2.2a1 1 0 0 1 1-.25 11.4 11.4 0 0 0 3.6.6 1 1 0 0 1 1 1V20a1 1 0 0 1-1 1A17 17 0 0 1 3 4a1 1 0 0 1 1-1h3.5a1 1 0 0 1 1 1c0 1.25.2 2.45.6 3.6a1 1 0 0 1-.25 1z"/></svg>
    555-014-2287
  </div>
  <div class="abs contact-item" style="left:952px">
    <svg width="13" height="12" viewBox="0 0 24 22"><path fill="#fff" d="M2 8 12 2l10 6v12H2z"/><path fill="#1d2b64" d="M4 9l8 6 8-6v10H4z"/></svg>
    inquiry@korvelps.example
  </div>
</div>

<header class="abs site-header">
  <div class="abs brand"><span class="mark"></span>Korvel Professional Services</div>
  <nav class="main-nav">
    <a class="active" style="left:547px">HOME</a>
    <a style="left:636px">ABOUT US</a>
    <a style="left:755px">SERVICES</a>
    <a style="left:872px">TESTIMONIALS</a>
    <a style="left:1025px">CONTACT US</a>
  </nav>
</header>
<div class="abs nav-marker"></div>

<div class="abs hero" role="img" aria-label="Photo of a business team meeting around a table with phones, tablets and printed charts"></div>
<svg class="abs hero-hex" viewBox="0 0 434 416" aria-hidden="true">
  <polygon points="108,0 326,0 434,208 326,416 108,416 0,208" fill="#1d2b64" fill-opacity=".72"/>
</svg>
<h1 class="abs hero-title">WE ARE AN<br>PROFESSIONAL<br>SERVICES COMPANY IN<br>IT/TELECOM SECTOR.</h1>
<div class="abs hero-dots"><span></span><span></span><span></span></div>

<h2 class="abs section-title" style="top:724px">ABOUT KORVEL <em>PROFESSIONAL SERVICES</em></h2>
<div class="abs divider" style="top:778px"></div>
<p class="abs lead" style="top:808px">Lorem ipsum dolor sit amet, consectetuer adipiscing elit, sed diam nonummy nibh euismod tincidunt ut laoreet dolore magna aliquam erat volutpat. Ut wisi enim ad minim veniam, quis nostrud exerci tation ullamcorper suscipit lobortis magna aliquam erat volutpat.</p>
<p class="abs about-text">Lorem ipsum dolor sit amet, consectetuer adipiscing elit, sed diam nonummy nibh euismod tincidunt ut laoreet dolore magna aliquam erat volutpat. Ut wisi enim ad minim veniam, quis nostrud exerci tation ullamcorper suscipit lobortis nisl ut aliquip ex ea commodo consequat. Duis autem vel eum iriure dolor in hendrerit in vulputate velit esse molestie consequat, vel illum dolore eu feugiat nulla facilisis at vero eros et accumsan et iusto odio dignissim qui blandit praesent luptatumLorem ipsum dolor sit amet, consectetuer adipiscing elit, sed diam nonummy nibh euismodLorem ipsum dolor sit amet, consectetuer adipiscing elit, sed diam nonummy nibh euismod tincidunt ut</p>
<div class="abs btn-more"><span class="icon"></span><span class="label">READ MORE</span></div>

<div class="abs video">
  <div class="abs frame" role="img" aria-label="Video still of a technician standing in a server room"></div>
  <div class="abs play"></div>
  <div class="abs controls">
    <svg class="abs" style="left:10px;top:8px" width="10" height="11" viewBox="0 0 10 11"><path d="M0 0 10 5.5 0 11z" fill="#fff"/></svg>
    <span class="abs time" style="left:42px">04:59</span>
    <div class="abs track"><span></span></div>
    <span class="abs time" style="left:256px">10:35</span>
    <svg class="abs" style="left:292px;top:8px" width="12" height="11" viewBox="0 0 12 11"><path d="M0 3h3l4-3v11L3 8H0z" fill="#fff"/></svg>
    <svg class="abs" style="left:326px;top:7px" width="12" height="12" viewBox="0 0 12 12"><path d="M0 0h4L0 4zM12 12H8l4-4z" fill="#fff"/></svg>
  </div>
</div>

<div class="abs services"></div>
<h2 class="abs section-title" style="top:1217px">OUR <em>SERVICES</em></h2>
<div class="abs divider on-grey" style="top:1271px"></div>
<p class="abs lead" style="top:1302px">Lorem ipsum dolor sit amet, consectetuer adipiscing elit, sed diam nonummy nibh euismod tincidunt ut laoreet dolore magna aliquam erat volutpat. Ut wisi enim ad minim veniam, quis nostrud exerci tation ullamcorper suscipit lobortis magna aliquam erat volutpat.</p>

<div class="abs service" style="left:90px;top:1400px">
  <svg width="128" height="144" viewBox="0 0 128 144">
    <polygon points="64,5 123,38 123,106 64,139 5,106 5,38" fill="#fff" stroke="#1d2b64" stroke-width="8"/>
    <polyline points="123,72 123,106 64,139 5,106 5,72" fill="none" stroke="#2676b9" stroke-width="8"/>
    <g fill="#1d2b64"><circle cx="64" cy="50" r="7"/><path d="M53 70a11 9 0 0 1 22 0z"/><circle cx="42" cy="80" r="7"/><path d="M31 100a11 9 0 0 1 22 0z"/><circle cx="86" cy="80" r="7"/><path d="M75 100a11 9 0 0 1 22 0z"/></g>
    <g fill="none" stroke="#2676b9" stroke-width="3"><path d="M44 58a26 26 0 0 0-8 14"/><path d="M84 58a26 26 0 0 1 8 14"/><path d="M52 104a26 26 0 0 0 24 0"/></g>
  </svg>
  <h3>Unified Communications<br>And Collaboration</h3>
</div>
<div class="abs service" style="left:352px;top:1400px">
  <svg width="128" height="144" viewBox="0 0 128 144">
    <polygon points="64,5 123,38 123,106 64,139 5,106 5,38" fill="#fff" stroke="#1d2b64" stroke-width="8"/>
    <polyline points="123,72 123,106 64,139 5,106 5,72" fill="none" stroke="#2676b9" stroke-width="8"/>
    <g stroke="#1d2b64" stroke-width="2.5" fill="none"><path d="M40 52 64 42 88 54 92 80 70 96 44 88 36 70z"/><path d="M64 42 64 70 40 52M64 70 88 54M64 70 92 80M64 70 70 96M64 70 44 88M64 70 36 70"/></g>
    <g fill="#1d2b64"><circle cx="64" cy="42" r="5"/><circle cx="40" cy="52" r="5"/><circle cx="88" cy="54" r="5"/><circle cx="92" cy="80" r="5"/><circle cx="44" cy="88" r="5"/><circle cx="36" cy="70" r="5"/><circle cx="64" cy="66" r="7"/><path d="M52 88a12 10 0 0 1 24 0v8H52z"/></g>
  </svg>
  <h3>Networking</h3>
</div>
<div class="abs service" style="left:612px;top:1400px">
  <svg width="128" height="144" viewBox="0 0 128 144">
    <polygon points="64,5 123,38 123,106 64,139 5,106 5,38" fill="#fff" stroke="#1d2b64" stroke-width="8"/>
    <polyline points="123,72 123,106 64,139 5,106 5,72" fill="none" stroke="#2676b9" stroke-width="8"/>
    <path d="M66 40c-17 0-28 12-28 27 0 7 3 12 6 16v17h22v-8h9c4 0 6-3 6-6v-7l6-2-6-10c0-16-6-27-15-27z" fill="#1d2b64"/>
    <circle cx="64" cy="64" r="9" fill="none" stroke="#fff" stroke-width="3"/>
    <path d="M64 55v18" stroke="#fff" stroke-width="3"/>
  </svg>
  <h3>Customer Experience<br>Management</h3>
</div>
<div class="abs service" style="left:882px;top:1400px">
  <svg width="128" height="144" viewBox="0 0 128 144">
    <polygon points="64,5 123,38 123,106 64,139 5,106 5,38" fill="#fff" stroke="#1d2b64" stroke-width="8"/>
    <polyline points="123,72 123,106 64,139 5,106 5,72" fill="none" stroke="#2676b9" stroke-width="8"/>
    <path d="M48 64a10 10 0 0 1 6-18 14 14 0 0 1 26 2 9 9 0 0 1 0 16z" fill="#1d2b64"/>
    <g stroke="#1d2b64" stroke-width="2.5" fill="none"><path d="M64 64v14M40 78h48M40 78v6M64 78v6M88 78v6"/></g>
    <g fill="none" stroke="#1d2b64" stroke-width="2.5"><rect x="30" y="84" width="20" height="14"/><rect x="54" y="84" width="20" height="14"/><rect x="78" y="84" width="20" height="14"/></g>
  </svg>
  <h3>Cloud</h3>
</div>

<div class="abs offer-card presales" style="left:80px">
  <div class="photo" role="img" aria-label="Photo of a hand holding a glowing globe surrounded by tablets">PRESALES SERVICES</div>
</div>
<div class="abs offer-card install" style="left:608px">
  <div class="photo" role="img" aria-label="Photo of a technician installing network cabling in a server rack">INSTALLATION SERVICES</div>
</div>

<div class="abs testimonials"></div>
<h2 class="abs section-title" style="top:2151px">CLIENT <em>TESTIMONIALS</em></h2>
<div class="abs divider on-grey" style="top:2205px"></div>

<svg class="abs arrow" style="left:167px" viewBox="0 0 16 30"><path d="M14 2 2 15l12 13" fill="none" stroke="#d0d0d0" stroke-width="2"/></svg>
<svg class="abs arrow" style="left:1015px" viewBox="0 0 16 30"><path d="M2 2l12 13L2 28" fill="none" stroke="#d0d0d0" stroke-width="2"/></svg>

<div class="abs client active" style="left:192px">
  <svg width="118" height="130" viewBox="0 0 118 130" role="img" aria-label="Portrait of client Mr. Tavin Orlecky">
    <polygon points="59,3 115,33 115,97 59,127 3,97 3,33" fill="#c4b7a6" stroke="#2676b9" stroke-width="5"/>
  </svg>
  <div class="name">Mr. Tavin Orlecky</div>
</div>
<div class="abs client" style="left:403px">
  <svg width="118" height="130" viewBox="0 0 118 130" role="img" aria-label="Portrait of client Mrs. Pella Rundquist">
    <polygon points="59,3 115,33 115,97 59,127 3,97 3,33" fill="#d8cbbd" stroke="#d4d4d4" stroke-width="5"/>
  </svg>
  <div class="name">Mrs. Pella Rundquist</div>
</div>
<div class="abs client" style="left:615px">
  <svg width="118" height="130" viewBox="0 0 118 130" role="img" aria-label="Portrait of client Mr. Doran Velisk">
    <polygon points="59,3 115,33 115,97 59,127 3,97 3,33" fill="#c9a98a" stroke="#d4d4d4" stroke-width="5"/>
  </svg>
  <div class="name">Mr. Doran Velisk</div>
</div>
<div class="abs client" style="left:826px">
  <svg width="118" height="130" viewBox="0 0 118 130" role="img" aria-label="Portrait of client Miss Ilsa Marrow">
    <polygon points="59,3 115,33 115,97 59,127 3,97 3,33" fill="#b99c84" stroke="#d4d4d4" stroke-width="5"/>
  </svg>
  <div class="name">Miss Ilsa Marrow</div>
</div>

<div class="abs quote-box">
  <span class="abs quote-mark" style="left:92px;top:14px">&ldquo;</span>
  <p>Lorem ipsum dolor sitamet, consectetuer adipiscing sed diam nonummy nibh euismod tincidunt ut laoreet dolore magna aliqua volutpat. Ut wisi enim ad minim veniam, quis nostrud exerci tation ullamcorper suscipit lobortis nisl ut aliquip ex ea commodo consequat. Duis autem vel eum iriure dolor in hendrerit in vulputate velit esse molestie consequat.ud exerci tation ullamcorper</p>
  <span class="abs quote-mark" style="left:918px;top:78px">&rdquo;</span>
</div>

<footer class="abs site-footer"></footer>

<div class="abs footer-col" style="left:80px;top:2675px;width:134px">
  <h4>QUICK <em>LINKS</em></h4>
  <ul class="quick-links" style="position:relative">
    <li class="current" style="top:13px">&bull; Home</li>
    <li style="top:53px">&bull; About Us</li>
    <li style="top:91px">&bull; Services</li>
    <li style="top:130px">&bull; Testimonials</li>
    <li style="top:170px">&bull; Contact Us</li>
  </ul>
</div>

<div class="abs footer-col" style="left:272px;top:2675px;width:250px">
  <h4>CONTACT <em>DETAILS</em></h4>
</div>
<div class="abs footer-text" style="left:276px;top:2723px;width:200px;font-family:'Exo 2',sans-serif;font-weight:700;font-size:15px;line-height:24px">KORVEL PROFESSIONAL SERVICES</div>
<div class="abs footer-text" style="left:276px;top:2772px;font-size:12px">4821 Harlow Ave. Brenton Vale, Lebanon.</div>
<div class="abs footer-text" style="left:276px;top:2826px;display:flex;align-items:center;gap:12px">
  <svg width="12" height="12" viewBox="0 0 24 24"><path fill="#fff" d="M6.6 10.8a15.1 15.1 0 0 0 6.6 6.6l2.2-2.2a1 1 0 0 1 1-.25 11.4 11.4 0 0 0 3.6.6 1 1 0 0 1 1 1V20a1 1 0 0 1-1 1A17 17 0 0 1 3 4a1 1 0 0 1 1-1h3.5a1 1 0 0 1 1 1c0 1.25.2 2.45.6 3.6a1 1 0 0 1-.25 1z"/></svg>555-014-2287
</div>
<div class="abs footer-text" style="left:276px;top:2878px;display:flex;align-items:center;gap:12px">
  <svg width="13" height="10" viewBox="0 0 26 20"><rect width="26" height="20" fill="#fff"/><path d="M0 0l13 11L26 0" fill="none" stroke="#1d2b64" stroke-width="2.5"/></svg>inquiry@korvelps.example
</div>

<div class="abs footer-col" style="left:580px;top:2675px;width:267px">
  <h4>QUICK <em>INQUIRY</em></h4>
</div>
<div class="abs field" style="top:2724px;height:36px">Name</div>
<div class="abs field" style="top:2768px;height:36px">Email</div>
<div class="abs field" style="top:2810px;height:46px">Message</div>
<div class="abs btn-submit">SUBMIT</div>

<div class="abs footer-brand"><span class="mark"></span>Korvel Professional Services</div>

<div class="abs bottom-bar">
  <span class="abs copy">Copyright &copy; 2017 KORVEL PROFESSIONAL SERVICES. All Right Reserved.</span>
  <span class="abs social" style="left:1022px" aria-label="Social profile link"></span>
  <span class="abs social" style="left:1056px" aria-label="Social profile link"></span>
  <span class="abs social" style="left:1092px" aria-label="Social profile link"></span>
</div>

</body>
</html>
```